Flavour Wheel - Illustrator Graph

I need my basic layout, from the sample I provided, turned into a professional looking flavour wheel.

I have attached a sample of a final design I like, but please use your own creativity also.

All the exact words I need are on the uploaded illustration.

I would need the file supplied to me in .ai

Industry/Entity Type

Wheel

Font styles to use
Sans Serif

Colors

Designer to choose colors to be used in the design.

Requirements
Must have
• Files must be supplied in .ai format with fonts not outlined.
• I need each segment separated so I can change the colours if needed myself.
Nice to have
• I like small white gaps between the sections.

```html
<!DOCTYPE html>
<html lang="en">
<head>
<meta charset="utf-8">
<title>Flavour Wheel</title>
<link rel="stylesheet" href="https://fonts.googleapis.com/css2?family=Montserrat:wght@500;600&family=PT+Sans+Narrow&display=swap">
<style>
  :root {
    --bg: #ffffff;
    --gap: #ffffff;
    --sour: #a87b66; --bitter: #c98467; --vinegary: #bf7a4b; --citrus: #744a26;
    --earthy: #dc1f2b; --floral: #e04c50; --herby: #ee6a4e; --nutty: #f06a4c; --buttery: #f7a12b;
    --sweet: #00aeef; --fruity-sweet: #1ea3b3; --sugary: #9fb0b0; --caramel: #0f73bc;
    --salty: #00a651; --charred: #33a553; --briney: #5f9f80;
    --savoury: #ec5b2e; --meatiness: #f79a83; --umami: #e65768;
    --spicy: #d91a6b; --chilli: #9a5c6e; --peppery: #e06f9d; --cajun: #df7d80;
    --smokey: #ecb31f; --woody: #dfbd2a; --fruity-smokey: #b49a33; --acrid: #efe622;
    --herb-list: #f06a4c; --spice-list: #d0145a; --savoury-list: #f06a6a;
  }
  html, body { margin: 0; padding: 0; overflow: hidden; background: var(--bg); }
  .canvas { width: 1200px; height: 1000px; display: block; }
  .segment { stroke: var(--gap); stroke-width: 4; stroke-linejoin: round; }
  .ring-label, .family-label {
    font-family: "Montserrat", sans-serif; fill: #fff;
    text-anchor: middle; dominant-baseline: central;
  }
  .ring-label { font-size: 21px; font-weight: 500; letter-spacing: 0.5px; }
  .family-label { font-size: 16px; font-weight: 500; }
  .note { font-family: "PT Sans Narrow", sans-serif; font-size: 16px; }
  .note-lg { font-size: 20px; }
  .note-xl { font-family: "PT Sans Narrow", sans-serif; font-size: 34px; }
  .heading { font-family: "PT Sans Narrow", sans-serif; font-size: 24px; }
</style>
</head>
<body>
<svg class="canvas" viewBox="0 0 1200 1000" xmlns="http://www.w3.org/2000/svg">
  <defs>
    <path id="outer-wedge" d="M -21.43 -135.31 L -39.89 -251.86 A 255 255 0 0 1 39.89 -251.86 L 21.43 -135.31 A 137 137 0 0 0 -21.43 -135.31 Z"/>
    <path id="family-wedge-2" d="M -17 -52.31 L -42.34 -130.3 A 137 137 0 0 1 42.34 -130.3 L 17 -52.31 A 55 55 0 0 0 -17 -52.31 Z"/>
    <path id="family-wedge-3" d="M -24.97 -49.01 L -62.2 -122.07 A 137 137 0 0 1 62.2 -122.07 L 24.97 -49.01 A 55 55 0 0 0 -24.97 -49.01 Z"/>
    <path id="family-wedge-4" d="M -32.33 -44.5 L -80.53 -110.84 A 137 137 0 0 1 80.53 -110.84 L 32.33 -44.5 A 55 55 0 0 0 -32.33 -44.5 Z"/>
  </defs>

  <g class="wheel" transform="translate(572 520)">
    <!-- flavour families -->
    <g class="families">
      <use class="segment family-sour" href="#family-wedge-3" transform="rotate(0)" style="fill:var(--sour)"/>
      <use class="segment family-earthy" href="#family-wedge-4" transform="rotate(63)" style="fill:var(--earthy)"/>
      <use class="segment family-sweet" href="#family-wedge-3" transform="rotate(126)" style="fill:var(--sweet)"/>
      <use class="segment family-salty" href="#family-wedge-2" transform="rotate(171)" style="fill:var(--salty)"/>
      <use class="segment family-savoury" href="#family-wedge-2" transform="rotate(207)" style="fill:var(--savoury)"/>
      <use class="segment family-spicy" href="#family-wedge-3" transform="rotate(252)" style="fill:var(--spicy)"/>
      <use class="segment family-smokey" href="#family-wedge-3" transform="rotate(306)" style="fill:var(--smokey)"/>
    </g>
    <!-- flavour notes -->
    <g class="notes">
      <use class="segment" href="#outer-wedge" transform="rotate(-18)" style="fill:var(--bitter)"/>
      <use class="segment" href="#outer-wedge" transform="rotate(0)" style="fill:var(--vinegary)"/>
      <use class="segment" href="#outer-wedge" transform="rotate(18)" style="fill:var(--citrus)"/>
      <use class="segment" href="#outer-wedge" transform="rotate(36)" style="fill:var(--floral)"/>
      <use class="segment" href="#outer-wedge" transform="rotate(54)" style="fill:var(--herby)"/>
      <use class="segment" href="#outer-wedge" transform="rotate(72)" style="fill:var(--nutty)"/>
      <use class="segment" href="#outer-wedge" transform="rotate(90)" style="fill:var(--buttery)"/>
      <use class="segment" href="#outer-wedge" transform="rotate(108)" style="fill:var(--fruity-sweet)"/>
      <use class="segment" href="#outer-wedge" transform="rotate(126)" style="fill:var(--sugary)"/>
      <use class="segment" href="#outer-wedge" transform="rotate(144)" style="fill:var(--caramel)"/>
      <use class="segment" href="#outer-wedge" transform="rotate(162)" style="fill:var(--charred)"/>
      <use class="segment" href="#outer-wedge" transform="rotate(180)" style="fill:var(--briney)"/>
      <use class="segment" href="#outer-wedge" transform="rotate(198)" style="fill:var(--meatiness)"/>
      <use class="segment" href="#outer-wedge" transform="rotate(216)" style="fill:var(--umami)"/>
      <use class="segment" href="#outer-wedge" transform="rotate(234)" style="fill:var(--chilli)"/>
      <use class="segment" href="#outer-wedge" transform="rotate(252)" style="fill:var(--peppery)"/>
      <use class="segment" href="#outer-wedge" transform="rotate(270)" style="fill:var(--cajun)"/>
      <use class="segment" href="#outer-wedge" transform="rotate(288)" style="fill:var(--woody)"/>
      <use class="segment" href="#outer-wedge" transform="rotate(306)" style="fill:var(--fruity-smokey)"/>
      <use class="segment" href="#outer-wedge" transform="rotate(324)" style="fill:var(--acrid)"/>
    </g>

    <g class="family-labels">
      <text class="family-label" transform="rotate(0) translate(0 -96) rotate(90)">Sour</text>
      <text class="family-label" transform="rotate(63) translate(0 -96) rotate(-90)">Earthy</text>
      <text class="family-label" transform="rotate(126) translate(0 -96) rotate(-90)">Sweet</text>
      <text class="family-label" transform="rotate(171) translate(0 -96) rotate(-90)">Salty</text>
      <text class="family-label" transform="rotate(207) translate(0 -96) rotate(90)">Savoury</text>
      <text class="family-label" transform="rotate(252) translate(0 -96) rotate(90)">Spicy</text>
      <text class="family-label" transform="rotate(306) translate(0 -96) rotate(90)">Smokey</text>
    </g>

    <g class="note-labels">
      <text class="ring-label" transform="rotate(-18) translate(0 -196) rotate(-90)">Bitter</text>
      <text class="ring-label" transform="rotate(0) translate(0 -196) rotate(-90)">Vinegary</text>
      <text class="ring-label" transform="rotate(18) translate(0 -196) rotate(-90)">Citrus</text>
      <text class="ring-label" transform="rotate(36) translate(0 -196) rotate(-90)">Floral</text>
      <text class="ring-label" transform="rotate(54) translate(0 -196) rotate(-90)">Herby</text>
      <text class="ring-label" transform="rotate(72) translate(0 -196) rotate(-90)">Nutty</text>
      <text class="ring-label" transform="rotate(90) translate(0 -196) rotate(-90)">Buttery</text>
      <text class="ring-label" transform="rotate(108) translate(0 -196) rotate(-90)">Fruity</text>
      <text class="ring-label" transform="rotate(126) translate(0 -196) rotate(-90)">Sugary</text>
      <text class="ring-label" transform="rotate(144) translate(0 -196) rotate(-90)">Caramel</text>
      <text class="ring-label" transform="rotate(162) translate(0 -196) rotate(-90)">Charred</text>
      <text class="ring-label" transform="rotate(180) translate(0 -196) rotate(-90)">Briney</text>
      <text class="ring-label" transform="rotate(198) translate(0 -196) rotate(-90)">Meatiness</text>
      <text class="ring-label" transform="rotate(216) translate(0 -196) rotate(90)">Umami</text>
      <text class="ring-label" transform="rotate(234) translate(0 -196) rotate(90)">Chilli</text>
      <text class="ring-label" transform="rotate(252) translate(0 -196) rotate(90)">Peppery</text>
      <text class="ring-label" transform="rotate(270) translate(0 -196) rotate(90)">Cajun</text>
      <text class="ring-label" transform="rotate(288) translate(0 -196) rotate(90)">Woody</text>
      <text class="ring-label" transform="rotate(306) translate(0 -196) rotate(90)">Fruity</text>
      <text class="ring-label" transform="rotate(324) translate(0 -196) rotate(90)">Acrid</text>
    </g>
  </g>

  <!-- ingredient lists -->
  <g class="ingredients">
    <g class="note" style="fill:var(--herb-list)">
      <text x="917" y="130" transform="rotate(50 917 130)">Sage</text>
      <text x="903" y="141" transform="rotate(50 903 141)">Oregano</text>
      <text x="891" y="153" transform="rotate(50 891 153)">Thyme</text>
      <text x="877" y="164" transform="rotate(50 877 164)">Rosemary</text>
      <text x="863" y="176" transform="rotate(50 863 176)">Bay Leaf</text>
      <text x="850" y="188" transform="rotate(50 850 188)">Fennel</text>
      <text x="836" y="200" transform="rotate(50 836 200)">Five Spice</text>
      <text x="824" y="213" transform="rotate(50 824 213)">Nutmeg</text>
      <text x="812" y="225" transform="rotate(50 812 225)">Tumeric</text>
      <text x="800" y="238" transform="rotate(50 800 238)">Star Anise</text>
      <text x="788" y="250" transform="rotate(50 788 250)">Cinnamin</text>
      <text x="776" y="263" transform="rotate(50 776 263)">Clove</text>
      <text x="765" y="276" transform="rotate(50 765 276)">Pecan</text>
      <text x="752" y="289" transform="rotate(50 752 289)">Coffee</text>
    </g>
    <g class="note" style="fill:var(--floral);font-size:18px">
      <text x="736" y="190" transform="rotate(55 736 190)">Coriander</text>
      <text x="719" y="214" transform="rotate(55 719 214)">Celery</text>
      <text x="702" y="240" transform="rotate(55 702 240)">Tea</text>
    </g>
    <g class="note note-lg" style="fill:var(--citrus)">
      <text x="655" y="152" transform="rotate(12 655 152)">Sumac</text>
      <text x="647" y="180" transform="rotate(12 647 180)">Zests</text>
      <text x="640" y="207" transform="rotate(12 640 207)">Lime</text>
      <text x="632" y="235" transform="rotate(12 632 235)">Lemon</text>
    </g>
    <g class="note" style="fill:var(--vinegary)">
      <text x="565" y="230" transform="rotate(-90 565 230)">Rice Vinegar</text>
      <text x="588" y="230" transform="rotate(-90 588 230)">Balsamic Vinegar</text>
      <text x="611" y="230" transform="rotate(-90 611 230)">Apple Cider Vinegar</text>
    </g>
    <g class="note" style="fill:var(--bitter)">
      <text x="428" y="187" transform="rotate(-12 428 187)">Tamarind</text>
      <text x="436" y="216" transform="rotate(-12 436 216)">Citric Acids</text>
      <text x="444" y="245" transform="rotate(-12 444 245)">Cocktail Bitters</text>
    </g>
    <text class="heading" x="364" y="298" transform="rotate(-30 364 298)" style="fill:var(--fruity-smokey)">Cresote</text>
    <g class="note" style="fill:var(--buttery);font-size:15px">
      <text x="224" y="318" transform="rotate(-55 224 318)">Bourbon</text>
      <text x="243" y="334" transform="rotate(-55 243 334)">Whiskey</text>
      <text x="262" y="350" transform="rotate(-55 262 350)">Charcoal</text>
      <text x="284" y="366" transform="rotate(-55 284 366)">Fruit Woods</text>
      <text x="304" y="383" transform="rotate(-55 304 383)">Hard Woods</text>
    </g>
    <text class="note-xl" x="842" y="413" transform="rotate(90 842 413)" style="fill:var(--buttery)">Butter</text>
    <g class="note" style="fill:var(--fruity-sweet);font-size:15px">
      <text x="866" y="592" transform="rotate(-90 866 592)">Fruit Juice</text>
      <text x="887" y="595" transform="rotate(-90 887 595)">Fruits</text>
      <text x="908" y="597" transform="rotate(-90 908 597)">Sauce</text>
      <text x="930" y="597" transform="rotate(-90 930 597)">Kethup</text>
    </g>
    <g class="note" style="fill:var(--sweet);font-size:15px">
      <text x="828" y="665" transform="rotate(-60 828 665)">Cola</text>
      <text x="852" y="677" transform="rotate(-60 852 677)">Agave Nectar</text>
      <text x="873" y="688" transform="rotate(-60 873 688)">Sugars</text>
    </g>
    <g class="note note-lg" style="fill:var(--caramel)">
      <text x="760" y="745" transform="rotate(-40 760 745)">Honey</text>
      <text x="783" y="766" transform="rotate(-40 783 766)">Molasses</text>
      <text x="805" y="788" transform="rotate(-40 805 788)">Maple Syrup</text>
    </g>
    <g class="note" style="fill:var(--salty)">
      <text x="676" y="796" transform="rotate(-20 676 796)">Anchovies</text>
      <text x="687" y="819" transform="rotate(-20 687 819)">Garlic</text>
      <text x="696" y="841" transform="rotate(-20 696 841)">Sea Salt</text>
      <text x="706" y="863" transform="rotate(-20 706 863)">Kosher Salt</text>
    </g>
    <g class="note" style="fill:var(--briney)">
      <text x="581" y="810" transform="rotate(-3 581 810)">Soy Sauce</text>
      <text x="583" y="838" transform="rotate(-3 583 838)">Fish Sauce</text>
      <text x="585" y="866" transform="rotate(-3 585 866)">Worcestershire</text>
    </g>
    <text class="heading" x="447" y="800" transform="rotate(15 447 800)" style="fill:var(--savoury)">Seasoning Sauce</text>
    <g class="note" style="fill:var(--savoury-list);font-size:15px">
      <text x="386" y="742" transform="rotate(45 386 742)">MSG</text>
      <text x="370" y="757" transform="rotate(45 370 757)">Vegespread</text>
      <text x="356" y="772" transform="rotate(45 356 772)">Lard</text>
      <text x="342" y="789" transform="rotate(45 342 789)">Stocks</text>
      <text x="327" y="806" transform="rotate(45 327 806)">Phosphates</text>
    </g>
    <g class="note" style="fill:var(--spice-list);font-size:15px">
      <text x="320" y="664" transform="rotate(55 320 664)">Onion</text>
      <text x="305" y="677" transform="rotate(55 305 677)">Szechuan</text>
      <text x="290" y="689" transform="rotate(55 290 689)">Allspice</text>
      <text x="276" y="701" transform="rotate(55 276 701)">Cumin</text>
      <text x="261" y="713" transform="rotate(55 261 713)">Pepper</text>
      <text x="245" y="725" transform="rotate(55 245 725)">Wasabi</text>
      <text x="225" y="737" transform="rotate(55 225 737)">Horseradish</text>
    </g>
    <g class="note" style="fill:var(--peppery);font-size:15px">
      <text x="280" y="580" transform="rotate(75 280 580)">Habanero</text>
      <text x="258" y="588" transform="rotate(75 258 588)">Hot Sauce</text>
      <text x="234" y="597" transform="rotate(75 234 597)">Jalapeno</text>
      <text x="210" y="605" transform="rotate(75 210 605)">Chipotle</text>
    </g>
    <g class="note" style="fill:var(--cajun);font-size:15px">
      <text x="213" y="557" transform="rotate(-82 213 557)">Paprika</text>
      <text x="244" y="557" transform="rotate(-82 244 557)">Mustard</text>
      <text x="276" y="560" transform="rotate(-82 276 560)">Red Pepper</text>
    </g>
  </g>
</svg>
</body>
</html>
```